Website Design for Harbor Trade Exchange! Buying Electronics Antiques Gold and valuables Online w/Cash

Our company gives people a reliable place to sell their old or un-needed valuables online where they can get a fair price and be involved in the decision upon the price to be paid. We provide prices for a huge variety of items ranging from Cell Phones, El

```html
<!DOCTYPE html>
<html lang="en">
<head>
<meta charset="utf-8">
<title>Harbor Trade Exchange</title>
<link href="https://fonts.googleapis.com/css2?family=Arimo:wght@400;700&family=Signika:wght@400;600&display=swap" rel="stylesheet">
<style>
:root{
  --navy:#27347f;
  --navy-deep:#1e2a6b;
  --band:#3f4fc4;
  --band-light:#5a6ad8;
  --royal:#2f3c9a;
  --red:#c8141e;
  --text:#333;
  --muted:#666;
  --panel:#ecedf5;
  --panel-blue:#e6e9fb;
  --chip:#8a93e6;
  --white:#fff;
  --rule:#c9cbd8;
}
*{box-sizing:border-box;margin:0;padding:0}
html,body{width:940px;height:1200px;overflow:hidden}
body{position:relative;background:linear-gradient(90deg,#2b3683,#35429a 50%,#2b3683);font-family:Arimo,Arial,sans-serif;color:var(--text)}
.abs{position:absolute}

/* header */
.site-header{left:92px;top:5px;width:756px;height:108px;background:linear-gradient(180deg,#2e3c9c,#1f2b78);box-shadow:0 3px 8px rgba(0,0,0,.5)}
.brand{left:20px;top:26px;font:700 31px/1.08 Arimo,sans-serif;color:var(--white);width:260px}
.package-link{left:430px;top:30px;color:var(--white);font-size:14px;display:flex;align-items:center;gap:10px;white-space:nowrap}
.follow{left:596px;top:32px;color:var(--white);font-size:11px;display:flex;align-items:center;gap:6px;white-space:nowrap}
.follow i{width:15px;height:15px;border-radius:50%;background:#c8cbe8;display:inline-block}
.main-nav{left:370px;top:63px;display:flex;box-shadow:0 1px 3px rgba(0,0,0,.4)}
.main-nav a{display:block;height:31px;line-height:31px;padding:0 12px;font-size:13px;color:#222;text-decoration:none;white-space:nowrap;background:linear-gradient(#fff,#dcdde4);border-right:1px solid #b8bbc8}
.main-nav a.active{background:linear-gradient(#e2262e,#b10f16);color:var(--white);padding:0 22px}

/* main panel */
.main-panel{left:92px;top:127px;width:756px;height:898px;background:var(--white)}
.quote-band{left:17px;top:16px;width:722px;height:85px;background:linear-gradient(180deg,var(--band-light),var(--band));color:#dfe3ff}
.quote-band label{position:absolute;font-size:12.5px;font-weight:700;white-space:nowrap}
.field{position:absolute;height:24px;background:var(--white);border:1px solid #9aa;font-size:10.5px;color:#888;line-height:22px;padding:0 7px;white-space:nowrap;overflow:hidden}
.btn-light{position:absolute;height:24px;background:linear-gradient(#fff,#cfd3f0);border:1px solid #7b84c8;font:700 11.5px/22px Arimo,sans-serif;color:var(--navy);text-align:center}
.or{position:absolute;left:330px;top:38px;font:700 22px Arimo,sans-serif;color:#9aa6f0}

.section-title{font:400 14.5px Arimo,sans-serif;color:var(--navy);text-transform:uppercase;white-space:nowrap}
.steps{left:17px;top:134px;width:540px;height:195px;background:linear-gradient(180deg,#fafafa,#e4e4e6)}
.step{position:absolute;top:0;width:180px;height:195px}
.step .num{position:absolute;left:2px;top:10px;font:700 66px Signika,sans-serif;color:#cfcfd3}
.step h3{position:absolute;left:43px;top:10px;font:600 18px Signika,sans-serif;color:var(--red);line-height:1;white-space:nowrap}
.step p{position:absolute;left:43px;top:31px;font:600 14px/1.1 Signika,sans-serif;color:var(--royal);white-space:nowrap}
.step .art{position:absolute;top:88px;height:92px}

.tabs{left:54px;top:374px;display:flex;gap:5px}
.tabs span{height:25px;line-height:25px;padding:0 9px;font-size:12px;color:#222;white-space:nowrap;border:1px solid #8e96d8;background:linear-gradient(#fff,#e2e4f2)}
.tabs span.active{background:var(--red);color:var(--white);border-color:var(--red)}
.product{position:absolute;top:411px;width:102px}
.product .thumb{height:73px;border:5px solid #e8e8ec;background:linear-gradient(135deg,#c9ccd6,#5d6378)}
.product p{margin-top:8px;font-size:11px;line-height:11px;color:#555;padding-left:6px}
.product p b{font-weight:400;color:var(--red)}
.arrow{position:absolute;top:410px;font:700 30px Arimo,sans-serif;color:var(--royal)}
.divider{left:17px;top:536px;width:540px;height:1px;background:var(--rule)}
.about p{font-size:10px;line-height:15px;color:#333;margin-bottom:4px}
.about b{font-weight:400;color:var(--red)}

.paid{left:17px;top:663px;width:540px;height:220px;background:var(--panel)}
.paid-row{position:absolute;left:16px;width:490px;height:40px;display:flex;align-items:center;border-bottom:1px dashed #c8c8d2}
.paid-row .pic{flex:none;width:48px;height:34px;border:1px solid #ccc;margin-right:18px}
.paid-row p{font-size:10.5px;color:var(--royal);white-space:nowrap}
.paid-row em{font-style:normal;font-weight:700;color:var(--red)}

/* sidebar */
.side-box{position:absolute;left:575px;width:164px;background:var(--panel)}
.side-box h4{font:700 15px Arimo,sans-serif;color:#222;line-height:1.1}
.cat-list a{display:flex;justify-content:space-between;align-items:center;width:128px;height:19px;margin-bottom:6px;background:var(--chip);color:var(--white);font-size:11.5px;padding:0 6px 0 15px;text-decoration:none}
.cat-list a i{width:11px;height:11px;border:1.5px solid var(--white);border-radius:2px}
.contact-form label{position:absolute;left:15px;font:700 9px Arimo,sans-serif;color:#444}
.contact-form .in{position:absolute;left:58px;width:93px;height:18px;border:1px solid #556;background:var(--white)}

/* footer */
.site-footer{left:0;top:1025px;width:940px;height:175px}
.foot-brand{left:112px;top:38px;width:95px;font:700 17px/1.2 Arimo,sans-serif;color:var(--white)}
.foot-col h5{font:400 11px Arimo,sans-serif;color:var(--white);margin-bottom:9px;white-space:nowrap}
.foot-col a{display:block;font-size:9.5px;color:#9ea6de;line-height:18.6px;text-decoration:none;white-space:nowrap}
.socials{left:668px;top:50px;display:flex;gap:6px}
.socials i{width:29px;height:29px;border-radius:50%;background:#d9dcf0;display:block}
.copyright{left:672px;top:103px;font-size:10px;line-height:13px;color:#8c94d2;white-space:nowrap}
</style>
</head>
<body>

<header class="site-header abs">
  <div class="brand abs">Harbor Trade Exchange</div>
  <div class="package-link abs">
    <svg width="20" height="20" viewBox="0 0 20 20"><path d="M3 5l7-3 7 3v10l-7 3-7-3z" fill="#fff"/><path d="M10 8v10M3 5l7 3 7-3" stroke="#2e3c9c" stroke-width="1.2" fill="none"/></svg>
    View Our Package
  </div>
  <div class="follow abs">Follow Us <i></i><i></i><i></i><i></i></div>
  <nav class="main-nav abs">
    <a class="active">Login</a><a>Sign Up</a><a>How It Works</a><a>Help</a><a>Contact</a>
  </nav>
</header>

<main class="main-panel abs">
  <section class="quote-band abs">
    <label style="left:15px;top:14px">Get an Instant Quote:</label>
    <div class="field" style="left:13px;top:34px;width:210px">Select Category</div>
    <svg class="abs" style="left:204px;top:38px" width="16" height="16" viewBox="0 0 16 16"><rect width="16" height="16" rx="2" fill="#1d2450"/><path d="M4 6h8l-4 5z" fill="#fff"/></svg>
    <div class="btn-light" style="left:229px;top:34px;width:74px">SEARCH</div>
    <div class="or">OR</div>
    <label style="left:382px;top:14px">Make an Offer:</label>
    <label style="left:551px;top:14px">Desired Price:</label>
    <div class="field" style="left:380px;top:34px;width:165px">Brief Item Description/Model No.</div>
    <div class="field" style="left:550px;top:34px;width:85px">$</div>
    <div class="btn-light" style="left:644px;top:34px;width:64px">SEND</div>
  </section>

  <h2 class="section-title abs" style="left:31px;top:112px">How It Works</h2>
  <section class="steps abs">
    <div class="step" style="left:0">
      <span class="num">1</span><h3>Get a Quote</h3><p>Or make an<br>offer</p>
      <div class="art" role="img" aria-label="Laptop showing the company site" style="left:12px;width:140px;background:linear-gradient(180deg,#d8d9dd,#9fa1a8)"></div>
    </div>
    <div class="step" style="left:180px">
      <span class="num">2</span><h3>Ship Package</h3><p>With a pre-paid<br>label</p>
      <div class="art" role="img" aria-label="Cardboard package with a sale tag" style="left:38px;width:112px;background:linear-gradient(135deg,#e8b458,#c08530)"></div>
    </div>
    <div class="step" style="left:360px">
      <span class="num">3</span><h3>Get Paid</h3><p>Right away</p>
      <div class="art" role="img" aria-label="Hand holding out cash" style="left:38px;width:118px;background:linear-gradient(135deg,#d9b49a,#9aa68a)"></div>
    </div>
    <svg class="abs" style="left:0;top:0" width="540" height="195"><path d="M165 0l20 97-20 98M345 0l20 97-20 98" stroke="#fff" stroke-width="4" fill="none"/></svg>
  </section>

  <h2 class="abs" style="left:54px;top:347px;font:400 14.5px Arimo,sans-serif;color:var(--navy);white-space:nowrap">PRODUCTS FOR SALE <small style="font-size:9.5px">( Find products by below categories )</small></h2>
  <div class="tabs abs"><span class="active">Cell Phones</span><span>Electronics</span><span style="padding:0 23px">Laptops</span><span style="padding:0 20px">Antiques</span><span style="padding:0 15px">Gold</span><span>Jewelry</span></div>
  <span class="arrow" style="left:13px">&#10094;</span>
  <div class="product" style="left:54px"><div class="thumb" role="img" aria-label="Slide phone"></div><p>Lorem ipsum dolor sit..<b>view details</b></p></div>
  <div class="product" style="left:174px"><div class="thumb" role="img" aria-label="Touchscreen phone"></div><p>Lorem ipsum dolor sit..<b>view details</b></p></div>
  <div class="product" style="left:294px"><div class="thumb" role="img" aria-label="Blue handset"></div><p>Lorem ipsum dolor sit..<b>view details</b></p></div>
  <div class="product" style="left:415px"><div class="thumb" role="img" aria-label="Silver smartphone"></div><p>Lorem ipsum dolor sit..<b>view details</b></p></div>
  <span class="arrow" style="left:535px">&#10095;</span>

  <div class="divider abs"></div>
  <section class="about abs" style="left:18px;top:548px;width:540px">
    <h2 class="section-title" style="margin-bottom:8px">About Harbor Trade Exchange</h2>
    <p>Lorem ipsum dolor sit amet, consectetur adipiscing elit. Mauris at quam nibh. Aliquam erat volutpat. Quisque metus diam, molestie eget iaculis non,</p>
    <p>Elementum eget libero. Fusce arcu leo, auctor luctus consequat non, pellentesque a risus. Nulla facilisi. Nullam nec neque arcu, quis dictum arcu. Ut leo mauris, semper non mattis at, convallis vitae risus. Aliquam erat volutpat. Curabitur luctus hendrerit nibh, sit amet varius sem sagittis sed. ...<b>More about us</b></p>
  </section>

  <section class="paid abs">
    <h2 class="abs" style="left:18px;top:13px;font:400 14.5px Arimo,sans-serif;color:var(--band)">WHO'S GETTING PAID</h2>
    <div class="paid-row" style="top:35px"><div class="pic" role="img" aria-label="Slide phone" style="background:linear-gradient(#888,#333)"></div><p><em>nikolas</em> just sold a Norvel Slide 4G lorem ipsum dolor site <em>for $60.00....</em></p></div>
    <div class="paid-row" style="top:77px"><div class="pic" role="img" aria-label="Gold chain" style="background:linear-gradient(#e8c45a,#a57a1c)"></div><p><em style="font-weight:400">David</em> just sold a Golden chain 10Grm lorem ipsum dolor site <em>for $510.00....</em></p></div>
    <div class="paid-row" style="top:120px"><div class="pic" role="img" aria-label="Red media player" style="background:linear-gradient(#e04c55,#a3141c)"></div><p><em>Ronald</em> just sold a Qoro Pod Touch 4th Generation 8GB lorem ipsum dolor <em>for $58.00....</em></p></div>
    <div class="paid-row" style="top:163px;border:0"><div class="pic" role="img" aria-label="Laptop" style="background:linear-gradient(#c3c8d6,#6c7388)"></div><p><em>nikolas</em> just sold a Norvel Laptop 4G lorem ipsum dolor site <em>for $60.00....</em></p></div>
  </section>

  <aside>
    <div class="side-box" style="top:118px;height:210px;padding:11px 0 0 15px">
      <h4>We will buy your</h4>
      <p style="font-size:9px;color:#444;margin:3px 0 9px;white-space:nowrap">Select the item you want to sell</p>
      <div class="cat-list"><a>Cell Phones<i></i></a><a>Electronics<i></i></a><a>Laptops<i></i></a><a>Antiques<i></i></a><a>Gold<i></i></a><a>Jewelry<i></i></a></div>
    </div>
    <div class="side-box" style="top:344px;height:138px;padding:12px 0 0 15px">
      <h4 style="font-size:14px">Pre-paid shipping<br>labels</h4>
      <p style="font-size:9px;line-height:12px;color:#333;margin-top:3px;width:125px">Americans with items to send the items to us for sell.</p>
      <p style="font:700 9px/11px Arimo,sans-serif;color:var(--red);margin-top:14px">click for<br>details</p>
      <div class="abs" role="img" aria-label="Stacked shipping boxes" style="left:65px;top:70px;width:99px;height:68px;background:linear-gradient(135deg,#e4b869,#8a6030)"></div>
    </div>
    <div class="side-box contact-form" style="top:497px;height:263px;background:var(--panel-blue);padding:12px 0 0 15px">
      <h4 style="color:var(--royal);font-size:14px">Need Help?<br>Contact Us Now</h4>
      <svg class="abs" style="left:128px;top:4px" width="34" height="30" viewBox="0 0 34 30"><path d="M2 12L20 2l12 14-18 12z" fill="#fff" stroke="#6a74c4"/><path d="M2 12l14 6 16-2" stroke="#6a74c4" fill="none"/></svg>
      <p style="font-size:8.5px;line-height:12px;color:#555;margin-top:4px;width:140px">For contact please fill up the form below and just it to us.We will reply you soon.</p>
      <label style="top:96px">Name</label><div class="in" style="top:93px"></div>
      <label style="top:123px">Email</label><div class="in" style="top:120px"></div>
      <label style="top:151px">Phone</label><div class="in" style="top:148px"></div>
      <label style="top:177px">Message</label><div class="in" style="top:175px;height:48px"></div>
      <div class="abs" style="left:118px;top:235px;width:33px;height:15px;background:var(--red);color:#fff;font:700 9.5px/15px Arimo,sans-serif;text-align:center">Send</div>
    </div>
    <div class="side-box" style="top:777px;height:105px;padding:12px 0 0 15px">
      <h4 style="font-size:14px">We Pay through</h4>
      <div class="abs" style="left:14px;top:38px;width:70px;height:25px;background:#1f4e8c"></div>
      <div class="abs" style="left:92px;top:37px;width:62px;height:24px;background:#f1f1f1;border:1px solid #bbb"></div>
      <div class="abs" style="left:14px;top:72px;width:72px;height:20px;background:#f4f4f4;border:1px solid #ccc"></div>
    </div>
  </aside>
</main>

<footer class="site-footer abs">
  <div class="foot-brand abs">Harbor Trade Exchange</div>
  <div class="foot-col abs" style="left:238px;top:30px"><h5>COMPANY</h5><a>Home</a><a>Sign Up</a><a>How It Works</a><a>Help</a><a>Contact</a></div>
  <div class="foot-col abs" style="left:338px;top:30px"><h5>WHAT WE BUY</h5><a>Electronics</a><a>Laptop</a><a>Gold</a><a>Cell phones</a><a>Antiques</a></div>
  <div class="foot-col abs" style="left:418px;top:30px"><h5>&nbsp;</h5><a>Electronics</a><a>Laptop</a><a>Gold</a><a>Cell phones</a><a>Antiques</a></div>
  <div class="foot-col abs" style="left:516px;top:30px"><h5>ABOUT US</h5><a>Tidewell For Good</a><a>Privacy Policy</a><a>Your CA Privacy Rights</a><a>Terms of Use</a><a>General Policies</a></div>
  <div class="socials abs"><i></i><i></i><i></i><i></i></div>
  <div class="copyright abs">&copy;2012 Harbor Trade Exchange<br>All Rights Reserved</div>
</footer>

</body>
</html>
```